Verpackungsdesign für Räucherstäbchen
Zielgruppe
Unsere Firma Lindenkram importiert hochwertige und reine Räucherstoffe aus entfernten Ländern. Dabei steht die Nachhaltigkeit und der faire Handel im Vordergrund. Unser Fokus ist dabei der Handel mit Weihrauch, den wir aus den Ursprungsländern importieren und an Großhändler, Händler und Endkunden weiterverkaufen. Seit einigen Jahren haben wir den Wunsch echte, natürliche Räucherstäbchen auf den Markt zu bringen. Dieses Projekt wurde nun umgesetzt.
Wir suchen ein Verpackungsdesign für unsere Räucherstäbchen. Die Räucherstäbchen sind absolut naturrein (95% aller Räucherstäbchen auf dem Markt sind es nicht), ohne Chemie, ohne Parfum, ohne Synthetik. Absolut rein, hergestellt aus besten Rohstoffen, teilweise direkt aus Deutschland.
Aufgabenstellung
Da die Räucherstäbchen auch in den Handel kommen werden, ist es am Besten, dass die Verpackung eine Faltschachtel ist mit den Maßen: 6cm Breite, 22cm Länge, 1,5cm Höhe
Die Schachtel sollte sehr natürlich ausschauen und die Farben nicht zu kräftig.
Es wird ein Logo darauf geben, das ich hochladen werde.
Farben sollten natürlich sein, Elegant und natürlich. Wir wissen nicht genau, wie die Verpackung aussehen soll, doch sicher ist, dass sie nicht zu überladen sein sollte. Die Verpackung sollte schlicht, natürlich und edel sein
Wir planen über 20 Sorten: Harze, Sandelholz, Patchouli etc.
Das Design der Verpackung sollte das berücksichtigen. Ein Design, das später an die verschiedenen Sorten angepasst werden kann
Für das Beispiel-Design:
Text auf der Vorderseite:
Räucherstäbchen
Weihrauch Afrika
Made with love in Germany
Natur pur
Rückseite:
Naturreine Räucherstäbchen hergestellt mit den reinsten Rohstoffen
Ohne chemische oder synthetische Zusätze, kein Parfum, keine Abbrennhilfe
Brenndauer: ca. 45- 60min
Eine Verpackung beinhaltet 10 Räucherstäbchen.
Hergestellt von:
Made by
Lindenkram
Birkenauer Weg 14
67391 Talhausen

```html
<!DOCTYPE html>
<html lang="de">
<head>
<meta charset="utf-8">
<title>Räucherstäbchen – Faltschachtel Weihrauch Afrika</title>
<link href="https://fonts.googleapis.com/css2?family=Alegreya:wght@400;700&family=Alegreya+Sans:wght@400;700&display=swap" rel="stylesheet">
<style>
  :root {
    --stage: #111111;
    --cut-line: #e8559c;
    --carton: #fdf0df;
    --carton-light: #fff8ee;
    --label: #fffaf2;
    --sage: #5f7d4c;
    --terracotta: #e2573a;
    --peach: #f6c79c;
    --apricot: #eea064;
    --gold-start: #e07a22;
    --gold-end: #f3b21c;
  }
  * { box-sizing: border-box; margin: 0; padding: 0; }
  html, body { width: 1200px; height: 848px; overflow: hidden; }
  body { background: var(--stage); position: relative; }

  .dieline { position: absolute; left: 365px; top: 34px; width: 466px; height: 780px; }
  .panel, .flap {
    position: absolute;
    border: 1px solid var(--cut-line);
    background: radial-gradient(ellipse at 40% 30%, var(--carton-light), var(--carton) 70%);
    overflow: hidden;
  }
  .panel { width: 187px; height: 686px; top: 46px; }
  .panel--back { left: 0; }
  .panel--front { left: 233px; }
  .flap--side { width: 46px; height: 686px; top: 46px; }
  .flap--glue { left: 187px; }
  .flap--right { left: 420px; }
  .flap--top { left: 233px; top: 0; width: 187px; height: 46px; }
  .flap--bottom { left: 233px; top: 732px; width: 187px; height: 47px; }
  .flap--side .leaf-field {
    position: absolute; left: 0; top: 0; width: 100%; height: 426px;
    background: linear-gradient(180deg, #fbe4cc 0%, #f8d2ab 60%, var(--carton) 100%);
  }

  .label-box {
    position: absolute; left: 10px; top: 0; width: 167px; height: 240px;
    background: var(--label);
  }
  .side-leaves {
    position: absolute; top: 0; width: 10px; height: 240px;
    background: linear-gradient(180deg, #f6cfa6, #f1b27d);
  }
  .side-leaves--left { left: 0; }
  .side-leaves--right { right: 0; }

  .blossom {
    position: absolute; left: 50%; transform: translate(-50%, -50%);
    border-radius: 50%;
  }
  .blossom--large { width: 24px; height: 24px; background: #c9d6bb; }
  .blossom--small { width: 11px; height: 11px; background: #f3b49a; }

  .center-line {
    position: absolute; left: 0; width: 100%; text-align: center;
    transform: translateY(-50%);
  }
  .product-title {
    font-family: "Alegreya", Georgia, serif;
    font-size: 22px; letter-spacing: 0.5px; color: var(--sage);
    line-height: 1;
  }
  .variety {
    font-family: "Alegreya", Georgia, serif;
    font-size: 16px; color: var(--terracotta); line-height: 1;
  }
  .gold-band {
    position: absolute; left: 10px; top: 240px; width: 167px; height: 13px;
    background: linear-gradient(90deg, var(--gold-start), var(--gold-end));
  }
  .leaf-illustration {
    position: absolute; left: 0; top: 253px; width: 100%; height: 173px;
    background: radial-gradient(ellipse at 45% 40%, var(--apricot) 0%, var(--peach) 45%, #fbe2c8 80%, var(--carton) 100%);
  }

  .claim {
    font-family: "Alegreya", Georgia, serif;
    font-size: 17px; color: var(--terracotta); line-height: 1;
  }
  .made-with-love {
    font-family: "Alegreya", Georgia, serif; font-weight: 700;
    font-size: 12px; color: var(--terracotta); line-height: 16px;
  }
  .brand-mark {
    position: absolute; left: 50%; top: 568px; width: 58px; height: 58px;
    transform: translateX(-50%);
    border: 1.5px solid var(--sage); border-radius: 50%;
  }
  .brand-name {
    font-family: "Alegreya", Georgia, serif; font-weight: 700;
    font-size: 13px; color: var(--sage); line-height: 1;
  }

  .product-info {
    position: absolute; left: 24px; top: 442px; width: 158px;
    font-family: "Alegreya Sans", Arial, sans-serif;
    font-size: 9.5px; line-height: 12.5px; color: var(--terracotta);
  }
  .product-info p + p { margin-top: 12px; }
  .product-info strong { font-weight: 700; }
</style>
</head>
<body>
  <div class="dieline">
    <div class="flap flap--top"></div>
    <div class="flap flap--bottom"></div>

    <section class="panel panel--back">
      <div class="side-leaves side-leaves--left" role="img" aria-label="Rankenmuster aus Blättern"></div>
      <div class="side-leaves side-leaves--right" role="img" aria-label="Rankenmuster aus Blättern"></div>
      <div class="label-box">
        <span class="blossom blossom--large" style="top:46px" role="img" aria-label="Blütenornament"></span>
        <div class="center-line product-title" style="top:85px">RÄUCHER</div>
        <div class="center-line product-title" style="top:114px">STÄBCHEN</div>
        <span class="blossom blossom--small" style="top:154px" role="img" aria-label="kleines Blütenornament"></span>
        <div class="center-line variety" style="top:189px">WEIHRAUCH</div>
        <div class="center-line variety" style="top:211px">AFRIKA</div>
      </div>
      <div class="gold-band"></div>
      <div class="leaf-illustration" role="img" aria-label="Ornamentale Blattranken in Orange- und Pfirsichtönen"></div>
      <div class="product-info">
        <p>Naturreine Räucherstäbchen<br>hergestellt mit den reinsten<br>Rohstoffen. Ohne chemische oder<br>synthetische Zusätze, kein Parfum,<br>keine Abbrennhilfe.</p>
        <p><strong>Brenndauer:</strong> ca. 45- 60min</p>
        <p>Eine Verpackung beinhaltet<br><strong>10 Räucherstäbchen.</strong></p>
        <p><strong>Hergestellt von:</strong></p>
        <p>Made by<br>Lindenkram<br>Birkenauer Weg 14<br>67391 Talhausen</p>
      </div>
    </section>

    <div class="flap flap--side flap--glue">
      <div class="leaf-field" role="img" aria-label="Blattmuster auf der Seitenlasche"></div>
    </div>

    <section class="panel panel--front">
      <div class="side-leaves side-leaves--left" role="img" aria-label="Rankenmuster aus Blättern"></div>
      <div class="side-leaves side-leaves--right" role="img" aria-label="Rankenmuster aus Blättern"></div>
      <div class="label-box">
        <span class="blossom blossom--large" style="top:46px" role="img" aria-label="Blütenornament"></span>
        <div class="center-line product-title" style="top:85px">RÄUCHER</div>
        <div class="center-line product-title" style="top:114px">STÄBCHEN</div>
        <span class="blossom blossom--small" style="top:154px" role="img" aria-label="kleines Blütenornament"></span>
        <div class="center-line variety" style="top:189px">WEIHRAUCH</div>
        <div class="center-line variety" style="top:211px">AFRIKA</div>
      </div>
      <div class="gold-band"></div>
      <div class="leaf-illustration" role="img" aria-label="Ornamentale Blattranken in Orange- und Pfirsichtönen"></div>
      <div class="center-line claim" style="top:456px">NATUR PUR</div>
      <span class="blossom blossom--small" style="top:485px" role="img" aria-label="kleines Blütenornament"></span>
      <div class="center-line made-with-love" style="top:521px">Made with love<br>in Germany</div>
      <span class="brand-mark"></span>
      <div class="center-line brand-name" style="top:646px">lindenkram.de</div>
    </section>

    <div class="flap flap--side flap--right">
      <div class="leaf-field" role="img" aria-label="Blattmuster auf der Seitenlasche"></div>
    </div>
  </div>
</body>
</html>
```